Business Card / Appointment Card for Physician

On one side it should give the logo, address, and contact information, and on the other side it should br an Appointment card.

One Side:
Logo (see attached files)
Board Certified American Orthopedic Surgery

1487 Harrowgate Ave.
Suite KM7
Bronx, NY 10527
Tel: (718) 552 - 1948
Fax: (718) 552 - 7210

628 Fourth Ave.
Suite 42
New York, NY 10087
Tel: (212) 734 - 2815

Second Side:
Appointment
give them a choice of Bronx or Mahattan office
For:
Date:
Time:

If you are unable to keep your appointment, please call (718) 263-5102 24hrs in advance.

Target Market(s)

People that need orthopedic surgery

Industry/Entity Type

Business

Contact Information for Business Card

smart and attractive

Requirements
Must have
• logo
• contact information on one side, appointment information on the other

```html
<!DOCTYPE html>
<html lang="en">
<head>
<meta charset="utf-8">
<title>Whitcombe Orthopaedics – Business &amp; Appointment Cards</title>
<link href="https://fonts.googleapis.com/css2?family=Open+Sans:wght@400;600&display=swap" rel="stylesheet">
<style>
  :root{
    --stage-top:#5a5a5a;
    --stage-bottom:#151515;
    --card:#ffffff;
    --card-tint:#f3f3f4;
    --art-light:#f1f1f2;
    --art-mid:#e4e4e6;
    --brand-blue:#1f6fb8;
    --rule-blue:#2f7ac0;
    --brand-green:#76b84a;
    --text:#3a3a3a;
    --muted:#555;
  }
  *{box-sizing:border-box;margin:0;padding:0}
  html,body{width:1200px;height:1200px;overflow:hidden}
  body{
    background:linear-gradient(180deg,var(--stage-top),var(--stage-bottom));
    font-family:"Open Sans",Arial,sans-serif;
    color:var(--text);
    position:relative;
  }
  .card{
    position:absolute;left:220px;width:760px;height:434px;
    background:var(--card);overflow:hidden;
    box-shadow:0 10px 30px rgba(0,0,0,.45);
  }
  .card--contact{top:120px}
  .card--appointment{top:620px}

  /* contact side */
  .contact-art{
    position:absolute;left:0;top:0;width:440px;height:100%;
    background:radial-gradient(ellipse at 35% 60%,var(--art-mid),var(--art-light) 60%,rgba(255,255,255,0) 100%);
  }
  .contact-info{position:absolute;right:48px;top:48px;width:360px;font-size:15px;line-height:1.5}
  .brand{display:flex;align-items:center;gap:10px;margin-bottom:8px}
  .brand__dot{width:26px;height:26px;border-radius:50%;background:var(--brand-blue);flex:none}
  .brand__name{color:var(--brand-blue);font-weight:600;font-size:22px;letter-spacing:.2px;text-transform:uppercase;white-space:nowrap}
  .credential{font-size:14px;color:var(--muted);margin-bottom:22px}
  .label{color:var(--brand-blue)}
  .phones{margin-bottom:14px}
  .office{margin-bottom:14px}
  .office-rule{border:0;border-top:1.5px solid var(--rule-blue);margin:10px 0 12px}

  /* appointment side */
  .appt-art{
    position:absolute;right:0;top:0;width:420px;height:100%;
    background:radial-gradient(ellipse at 55% 45%,var(--art-light),rgba(255,255,255,0) 70%);
  }
  .appt-brand{position:absolute;right:40px;top:50px}
  .appt-brand .brand__name{font-size:20px}
  .appt-title{position:absolute;left:44px;top:40px;color:var(--brand-green);font-size:34px;font-weight:400}
  .appt-office{position:absolute;left:44px;top:100px;font-size:15px}
  .appt-box{position:absolute;left:44px;top:132px;width:420px;height:44px;border:1.5px solid #888}
  .appt-row{position:absolute;left:44px;font-size:19px;display:flex;align-items:baseline;gap:6px}
  .appt-row--1{top:200px}
  .appt-row--2{top:252px}
  .dots{display:inline-block;width:150px;border-bottom:2px dotted #555}
  .dots--time{width:140px}
  .appt-notice{
    position:absolute;left:0;right:0;bottom:30px;height:48px;
    background:var(--brand-green);color:#fff;font-size:16px;
    display:flex;align-items:center;justify-content:center;
  }
</style>
</head>
<body>

<section class="card card--contact">
  <div class="contact-art" role="img" aria-label="Faint line illustration of a knee joint"></div>
  <div class="contact-info">
    <div class="brand"><span class="brand__dot"></span><span class="brand__name">Daniel R. Whitcombe MD PC</span></div>
    <p class="credential">Board Certified American Orthopedic Surgery</p>
    <div class="phones">
      <p><span class="label">Tel:</span> (718) 552 - 1948</p>
      <p><span class="label">Fax:</span> (718) 552 - 7210</p>
    </div>
    <div class="office">
      <p>1487 Harrowgate Ave.</p>
      <p>Suite KM7, Bronx, NY 10527</p>
    </div>
    <hr class="office-rule">
    <div class="office">
      <p>628 Fourth Ave. Suite 42</p>
      <p>New York, NY 10087 | <span class="label">Tel:</span> (212) 734 - 2815</p>
    </div>
  </div>
</section>

<section class="card card--appointment">
  <div class="appt-art" role="img" aria-label="Faint line illustration of a shoulder joint"></div>
  <div class="appt-brand brand"><span class="brand__dot"></span><span class="brand__name">Daniel R. Whitcombe MD PC</span></div>
  <h2 class="appt-title">Appointment</h2>
  <p class="appt-office">give them a choice of Bronx or Mahattan office For:</p>
  <div class="appt-box"></div>
  <p class="appt-row appt-row--1">Date: <span class="dots"></span> Time: <span class="dots dots--time"></span></p>
  <p class="appt-row appt-row--2">Date: <span class="dots"></span> Time: <span class="dots dots--time"></span></p>
  <p class="appt-notice">If you are unable to keep your appointment, please call (718) 263-5102 24hrs in advance.</p>
</section>

</body>
</html>
```